Business Image

I have recently had a new company logo made up and require some new business cards to go with it.

Target Market(s)

Developers & high worth clients.

Industry/Entity Type

Business

Contact Information for Business Card

The business is in the construction/management industry. It needs to be classy but have a industrial feel. I would like the business card to be a elegant presentation in itself.

Requirements
Must have
• Current logo & company name. Colouring needs to be the same as the current design also.
Nice to have
• A few different designs & presentations of single and double sided business cards.

```html
<!DOCTYPE html>
<html lang="en">
<head>
<meta charset="utf-8">
<title>Meridian Build Partners – Business Card</title>
<link rel="stylesheet" href="https://fonts.googleapis.com/css2?family=Roboto:ital,wght@0,400;0,500;0,700;1,700&family=Roboto+Condensed:wght@700&display=swap">
<style>
  :root {
    --backdrop: #e4e5e7;
    --card: #f3f3f2;
    --brand-blue: #1f5582;
    --ink: #3c3c3c;
    --muted: #555555;
    --rule: #a9a9a9;
    --ghost: #dcdfe3;
    --white: #ffffff;
  }
  * { margin: 0; padding: 0; box-sizing: border-box; }
  html, body { width: 1200px; height: 960px; overflow: hidden; }
  body {
    background: var(--backdrop);
    font-family: "Roboto", Arial, sans-serif;
    color: var(--ink);
    position: relative;
  }
  .card {
    position: absolute;
    width: 600px;
    height: 342px;
    background: var(--card);
    border-radius: 22px;
    overflow: hidden;
  }
  .card--front { left: 314px; top: 113px; }
  .card--back  { left: 311px; top: 472px; }

  .wordmark {
    position: absolute;
    text-align: right;
    color: var(--brand-blue);
    font-family: "Roboto", Arial, sans-serif;
    font-weight: 500;
    line-height: 1;
  }
  .wordmark__main { display: block; letter-spacing: 1px; }
  .wordmark__sub  { display: block; letter-spacing: 2.4px; }
  .card--front .wordmark { right: 37px; top: 104px; }
  .card--front .wordmark__main { font-size: 29px; }
  .card--front .wordmark__sub  { font-size: 11px; margin-top: 5px; }
  .brand-square {
    position: absolute;
    right: 92px;
    top: 28px;
    width: 58px;
    height: 58px;
    background: var(--brand-blue);
  }

  .person { position: absolute; left: 33px; top: 148px; }
  .person__name {
    font-family: "Roboto Condensed", "Arial Narrow", sans-serif;
    font-weight: 700;
    font-size: 22px;
    color: var(--brand-blue);
    letter-spacing: 0.3px;
  }
  .person__title { font-size: 14px; font-weight: 500; color: var(--ink); margin-top: 2px; }

  .divider {
    position: absolute;
    left: 33px; right: 38px; top: 198px;
    height: 1px;
    background: var(--rule);
  }

  .phones { position: absolute; left: 33px; top: 209px; list-style: none; }
  .phones li {
    display: flex; align-items: center; gap: 8px;
    font-size: 14px; line-height: 19.5px; color: var(--muted);
  }
  .phones svg { width: 14px; height: 14px; fill: var(--brand-blue); }

  .address {
    position: absolute; right: 37px; top: 209px;
    text-align: right; font-style: normal;
    font-size: 14px; line-height: 19.5px; color: var(--muted);
  }

  .web-band {
    position: absolute; left: 0; right: 0; top: 291px;
    height: 29px;
    background: var(--brand-blue);
  }
  .web-band__url {
    position: absolute; left: 123px; top: 6px;
    color: var(--white);
    font-size: 13px; font-weight: 700; font-style: italic;
    letter-spacing: 2.6px;
  }

  .ghost-block {
    position: absolute;
    left: -40px; top: 10px;
    width: 330px; height: 330px;
    background: var(--ghost);
    opacity: 0.7;
  }
  .card--back .wordmark { right: 26px; top: 244px; }
  .card--back .wordmark__main { font-size: 36px; }
  .card--back .wordmark__sub  { font-size: 15px; margin-top: 6px; letter-spacing: 2.6px; }
  .card--back .back-url {
    position: absolute; right: 27px; top: 307px;
    font-size: 14px; color: var(--muted);
  }
</style>
</head>
<body>

<section class="card card--front" aria-label="Business card front">
  <div class="brand-square"></div>
  <div class="wordmark">
    <span class="wordmark__main">MERIDIAN</span>
    <span class="wordmark__sub">BUILD PARTNERS</span>
  </div>

  <div class="person">
    <div class="person__name">DANIEL HARROW</div>
    <div class="person__title">CEO/FOUNDER</div>
  </div>

  <div class="divider"></div>

  <ul class="phones">
    <li>
      <svg viewBox="0 0 24 24" aria-hidden="true"><path d="M6.6 10.8a15.1 15.1 0 0 0 6.6 6.6l2.2-2.2c.3-.3.7-.4 1-.2 1.1.4 2.3.6 3.6.6.6 0 1 .4 1 1V20c0 .6-.4 1-1 1A17 17 0 0 1 3 4c0-.6.4-1 1-1h3.5c.6 0 1 .4 1 1 0 1.3.2 2.5.6 3.6.1.3 0 .7-.2 1z"/></svg>
      555.214.3870
    </li>
    <li>
      <svg viewBox="0 0 24 24" aria-hidden="true"><path d="M7 1h10a2 2 0 0 1 2 2v18a2 2 0 0 1-2 2H7a2 2 0 0 1-2-2V3a2 2 0 0 1 2-2zm0 3v14h10V4zm5 15.5a1.2 1.2 0 1 0 0 2.4 1.2 1.2 0 0 0 0-2.4z"/></svg>
      555.309.6142
    </li>
    <li>
      <svg viewBox="0 0 24 24" aria-hidden="true"><path d="M6 2h12v6H6zM3 9h18a2 2 0 0 1 2 2v7h-4v4H5v-4H1v-7a2 2 0 0 1 2-2zm4 8v3h10v-3z"/></svg>
      555.472.8815
    </li>
  </ul>

  <address class="address">
    1420 Ironwood Drive<br>
    Granite Falls, Oregon 97120<br>
    daniel@meridianbp.com
  </address>

  <div class="web-band">
    <span class="web-band__url">www.meridianbp.com</span>
  </div>
</section>

<section class="card card--back" aria-label="Business card back">
  <div class="ghost-block"></div>
  <div class="wordmark">
    <span class="wordmark__main">MERIDIAN</span>
    <span class="wordmark__sub">BUILD PARTNERS</span>
  </div>
  <div class="back-url">www.meridianbuildpartners.com</div>
</section>

</body>
</html>
```